Home Page Redesign for Pet Website

Looking to redesign the home page of our WORDPRESS website which will be renamed The Animal Cover Handbook 2015.

Looking for clean design which communicates clarity.
Updates

This is for a Wordpress site.

Please note that the design MUST include the content which is shown in the table in the brief!

Hi Thanks for the designs so far. We have just updated the brief to provide more information and clarify a few issues. We have also now included a couple of layout suggestions. They are just suggestions but it should give you a better idea of what we are looking for. And we have just increased the budget for 1st place by £120. Please feel free to message me if you have any questions. Many thanks. Mabel

Please note that the new brief is in a file dated 25 Jan!

Project Deadline Extended
Reason: We have extended the deadline so we can continue working with the designers who have submitted designs we like. If you have any new designs please submit them by the original deadline of 7.37pm this evening (GMT). We are planning to make our final decision by Friday this week.

Target Market(s)

UK pet owners. All ages but largest age group is 35-50.

Industry/Entity Type

Insurance

Requirements
Must have
• Three clear content groups - LEARN, RESEARCH, CAMPAIGN (see brief for more details).
Stock photos with dogs and cats
Use current colour scheme
Must work with existing inner pages.
Existing font.. but 1pt larger
See brief for more details
Should not have
• Logo
Content from Existing Page (except for footer content... and menu headings).

```html
<!DOCTYPE html>
<html lang="en">
<head>
<meta charset="utf-8">
<title>The Animal Cover Handbook 2015</title>
<link href="https://fonts.googleapis.com/css2?family=Roboto+Slab:wght@400;700&family=Open+Sans:ital,wght@0,400;0,600;1,600&family=Arimo:wght@400;700&display=swap" rel="stylesheet">
<style>
:root{
  --sky:#4d94e8;
  --navy:#0b5aa6;
  --aqua:#17b2d5;
  --green:#5aa974;
  --orange:#f07b2e;
  --ink:#222;
  --line:#d6d6d6;
  --black:#0d0d0d;
  --wine:#b3233b;
  --taupe:#8a7d6e;
}
*{box-sizing:border-box;margin:0;padding:0}
html,body{width:695px;height:1200px;overflow:hidden}
body{position:relative;background:#fff;font-family:"Open Sans",Arial,sans-serif;color:var(--ink)}
.abs{position:absolute}
.top-rule{left:0;top:0;width:695px;height:2px;background:var(--sky)}
.site-title{left:86px;top:10px;font:700 16px "Roboto Slab",serif;color:#111;letter-spacing:.2px;white-space:nowrap}
.site-title span{color:var(--sky)}
.tagline{left:86px;top:36px;font:400 8.5px "Roboto Slab",serif;color:#222}
.phone{left:513px;top:9px;font:400 12px Arimo,sans-serif;color:#222;display:flex;align-items:center;gap:4px}
.search{left:462px;top:32px;width:117px;height:15px;border:1px solid #ccc;font:6px Arimo,sans-serif;color:#aaa;padding:3px 4px}
.go{left:584px;top:32px;width:24px;height:15px;background:var(--sky);color:#111;font:700 8px Arimo,sans-serif;text-align:center;line-height:15px}
.nav{left:0;top:54px;width:695px;height:28px;background:var(--sky)}
.nav a{position:absolute;top:9px;font:400 8.2px Arimo,sans-serif;color:#fff;text-decoration:none;white-space:nowrap}
.nav a.active{color:#111}
.nav .sep{position:absolute;top:0;width:1px;height:28px;background:rgba(255,255,255,.35)}
.hero{left:0;top:82px;width:695px;height:190px;background:var(--black)}
.hero-photo{left:85px;top:82px;width:524px;height:190px;background:linear-gradient(90deg,#fbf6ef 0%,#f4e3c9 20%,#ffffff 45%,#f1e2cc 70%,#ffffff 100%)}
.hero-caption{left:85px;top:249px;width:524px;height:23px;background:rgba(80,80,80,.75);color:#fff;font:400 14.5px "Roboto Slab",serif;text-align:center;line-height:23px}
.arrow{top:165px;width:18px;height:18px;display:flex;align-items:center;justify-content:center}
.arrow.left{left:66px;background:#8a8a8a}
.arrow.right{left:608px;background:var(--sky)}
.panel{left:79px;width:338px;color:#fff;padding:6px 7px}
.panel h2{font:400 10px "Roboto Slab",serif;padding-bottom:4px;border-bottom:1px solid rgba(255,255,255,.3);width:205px;margin-bottom:5px}
.panel h2 b{font-weight:700}
.panel p{font:400 6.8px/1.5 Arimo,sans-serif}
.learn{top:293px;height:155px;background:var(--navy)}
.research{top:464px;height:213px;background:var(--aqua)}
.campaign{top:693px;height:149px;background:var(--green)}
.cols{display:grid;grid-template-columns:168px 160px;margin-top:8px}
.bul{list-style:none}
.bul li{position:relative;padding-left:13px;font:400 7.3px "Open Sans",sans-serif;margin-bottom:5.6px;line-height:1.25}
.bul li::before{content:"";position:absolute;left:1px;top:1.5px;width:4px;height:4px;border-radius:50%;background:var(--orange);border:1.5px solid #fff;box-shadow:0 0 0 1px var(--orange)}
.research .bul li{margin-bottom:5.2px}
.research .sub{font:400 7.3px Arimo,sans-serif;margin-top:2px}
.research .cta{font:italic 600 9px/1.6 "Open Sans",sans-serif;margin-top:4px;color:#1a3350}
.more{position:absolute;right:13px;font:700 7.5px "Roboto Slab",serif;color:#fff;border-bottom:1px solid #fff;padding-bottom:1px}
.campaign p{font:400 7.3px/1.42 "Open Sans",sans-serif;margin-bottom:6px}
.popular{left:79px;top:859px;width:338px;height:71px;border:1px solid var(--line);padding:6px 7px;background:#fff}
.popular h2{font:400 10px "Roboto Slab",serif;color:#222;border-bottom:1px solid #e3e3e3;padding-bottom:3px;width:205px;margin-bottom:4px}
.popular h2 span{color:var(--sky)}
.popular p{font:400 7.3px/1.4 "Open Sans",sans-serif;color:#333}
.popular .row{display:flex;gap:24px;margin-top:4px}
.popular .row span{position:relative;padding-left:10px;font:400 7.8px "Open Sans",sans-serif;color:#333}
.popular .row span::before{content:"";position:absolute;left:0;top:2.5px;width:3px;height:3px;border-radius:50%;background:#fff;border:1.5px solid var(--orange)}
.more.dark{color:var(--sky);border-color:var(--sky);font-weight:400}
.ad{left:432px;width:176px;height:156px;background:#fbf8f3;border:1px solid #ccc;padding:6px 6px}
.ad .brand{font:700 15px "Roboto Slab",serif;color:var(--taupe);text-align:center;line-height:1.2}
.ad .slogan{font:400 8px "Roboto Slab",serif;color:#777;text-align:center;margin-top:2px}
.ad .pup{position:absolute;left:6px;top:44px;width:68px;height:84px;background:radial-gradient(circle at 45% 45%,#b5753c,#7a4b24 60%,#fbf8f3 75%)}
.ad ul{position:absolute;left:82px;top:50px;list-style:none}
.ad li{display:flex;align-items:center;gap:4px;font:700 8px/1.1 Arimo,sans-serif;color:var(--wine);margin-bottom:8px;white-space:nowrap}
.ad .quote{position:absolute;left:88px;top:111px;width:72px;height:17px;background:var(--wine);color:#fff;font:700 7.5px Arimo,sans-serif;text-align:center;line-height:17px;border-radius:2px}
.ad .offer{position:absolute;left:80px;top:133px;font:700 7.5px Arimo,sans-serif;color:#111;white-space:nowrap}
.ad .fine{position:absolute;left:0;width:174px;text-align:center;top:145px;font:400 5.5px Arimo,sans-serif;color:#777}
.ad.small{height:116px;padding-top:4px}
.ad.small .brand{font-size:13px}
.ad.small .slogan{font-size:7.5px;margin-top:0}
.ad.small .pup{top:32px;height:66px;width:62px}
.ad.small ul{top:38px}
.ad.small li{font-size:7px;margin-bottom:6px}
.ad.small .quote{top:84px;height:13px;line-height:13px;font-size:6.5px}
.ad.small .offer{top:99px;font-size:6.8px}
.ad.small .fine{top:108px;font-size:5px}
.card{left:430px;width:178px;background:#fff;border:1px solid var(--line);border-radius:3px;padding:4px 7px;box-shadow:0 6px 8px -6px rgba(0,0,0,.25)}
.card h3{font:400 10px "Roboto Slab",serif;color:#222;border-bottom:1px solid #e6e6e6;padding-bottom:3px;margin-bottom:5px}
.bio{top:465px;height:173px}
.bio .portrait{position:absolute;left:10px;top:26px;width:50px;height:50px;border-radius:50%;background:radial-gradient(circle,#8a6a45,#c7d7e3 70%)}
.bio .who{position:absolute;left:88px;top:30px;font:400 7.3px Arimo,sans-serif;color:#222;line-height:1.3}
.bio .who2{position:absolute;left:88px;top:63px;font:400 7.3px Arimo,sans-serif;color:#222}
.bio .txt{position:absolute;left:7px;top:84px;width:164px;font:400 6.3px/1.65 Arimo,sans-serif;color:#333}
.bio .txt p{margin-bottom:2px}
.disc{top:657px;height:139px}
.disc p{font:400 6.6px/1.6 "Open Sans",sans-serif;color:#222}
.disc .see{font-weight:600;margin-top:3px}
.pet-left{left:14px;top:872px;width:50px;height:82px;background:linear-gradient(180deg,#5a3d22,#b0793f 60%,#8c5a2c)}
.pet-right{left:608px;top:836px;width:87px;height:118px;background:linear-gradient(180deg,#c9b6a0,#8e7560 55%,#5b4637)}
.footer{left:0;top:954px;width:695px;height:222px;background:var(--sky)}
.widget{top:970px;width:152px;height:190px;background:#fff;border-radius:3px;overflow:hidden}
.widget .head{height:20px;font:700 9.5px Arimo,sans-serif;color:#2b4a84;padding:5px 8px;background:#dfe6f1}
.fb{left:91px}
.tw{left:266px}
.tw .head{background:#6ccbe0;color:#fff}
.avatar{width:22px;height:22px;background:linear-gradient(#a88e78,#5e4a3c);flex:none}
.fb .page{display:flex;gap:6px;padding:6px;border-bottom:1px solid #e2e2e2}
.fb .name{font:400 7px Arimo,sans-serif;color:#3b5998}
.likebtn{display:inline-block;background:#4e69a2;color:#fff;font:700 6px Arimo,sans-serif;padding:1px 4px;margin-top:3px}
.fb .post{margin:6px;border:1px solid #e2e2e2;padding:5px;height:122px;overflow:hidden;font:400 6.2px/1.5 Arimo,sans-serif;color:#333}
.fb .post .meta{display:flex;gap:6px;margin-bottom:6px}
.fb .post .meta small{display:block;color:#999;font-size:5px}
.tw .bar{display:flex;justify-content:space-between;padding:5px;font:700 6.8px Arimo,sans-serif;border-bottom:1px solid #e2e2e2}
.tw .bar span{font:400 5.5px Arimo,sans-serif;border:1px solid #ccc;border-radius:2px;padding:1px 4px;color:#333}
.tweet{display:flex;gap:4px;padding:5px;font:400 5.8px/1.45 Arimo,sans-serif;color:#333;border-bottom:1px solid #eee}
.tweet .avatar{width:14px;height:14px}
.tweet .body{flex:1}
.tweet .top{display:flex;justify-content:space-between}
.tweet b{font-size:6px}
.tweet a{color:#2a7ab0;text-decoration:none}
.tweet .dim{color:#999}
.tw .input{position:absolute;left:3px;bottom:4px;width:146px;height:15px;border:1px solid #ccc;font:400 6px Arimo,sans-serif;color:#666;padding:3px 4px}
.follow-title{left:443px;top:963px;font:400 10px "Roboto Slab",serif;color:#111}
.sbtn{left:443px;height:17px;background:#f3f5f8;border:1px solid #b9c2cf;border-radius:2px;font:700 9px Arimo,sans-serif;color:#2d3e57;display:flex;align-items:center;gap:4px;padding:0 5px;white-space:nowrap}
.sbtn i{width:9px;height:9px;background:var(--sky);display:block}
.foot-title{left:430px;top:1110px;width:186px;text-align:center;font:700 14.5px/1.25 "Roboto Slab",serif;color:#111}
.copy{left:0;top:1176px;width:695px;height:24px;background:var(--black);color:#ddd;font:400 6px Arimo,sans-serif;text-align:center;line-height:24px}
</style>
</head>
<body>
<div class="abs top-rule"></div>

<header>
  <div class="abs site-title">THE ANIMAL COVER <span>HANDBOOK 2015</span></div>
  <div class="abs tagline">Independent Unbiased Information For Fellow Pet Owners</div>
  <div class="abs phone">
    <svg width="11" height="11" viewBox="0 0 12 12"><circle cx="6" cy="6" r="5.3" fill="none" stroke="#222" stroke-width="1"/><path d="M4 3.2c.4-.3.8-.2 1 .2l.5 1c.1.3 0 .5-.2.7l-.3.3c.3.7.8 1.2 1.5 1.5l.3-.3c.2-.2.4-.3.7-.2l1 .5c.4.2.5.6.2 1-.6.8-1.5.9-2.6.2C4.9 7.5 4.2 6.7 3.8 5.7 3.4 4.6 3.4 3.8 4 3.2z" fill="#222"/></svg>
    123-456-7890
  </div>
  <div class="abs search">search here......</div>
  <div class="abs go">GO</div>
</header>

<nav class="abs nav">
  <a class="active" style="left:92px">HOME</a>
  <a style="left:134px">LEARN About Pet Insurance</a>
  <span class="sep" style="left:245px"></span>
  <a style="left:254px">RESEARCH Pet Insurance Policies</a>
  <span class="sep" style="left:390px"></span>
  <a style="left:399px">CAMPAIGN For Fairer Pet Insurance</a>
  <span class="sep" style="left:540px"></span>
  <a style="left:550px">CONTACT US</a>
</nav>

<section>
  <div class="abs hero"></div>
  <div class="abs hero-photo" role="img" aria-label="Two spaniel puppies sitting beside a kitten and a black cat on a white background"></div>
  <div class="abs hero-caption">Independent Unbiased Information For Fellow Pet Owners</div>
  <div class="abs arrow left"><svg width="8" height="10" viewBox="0 0 8 10"><path d="M6 1L2 5l4 4" stroke="#fff" stroke-width="1.6" fill="none"/></svg></div>
  <div class="abs arrow right"><svg width="8" height="10" viewBox="0 0 8 10"><path d="M2 1l4 4-4 4" stroke="#fff" stroke-width="1.6" fill="none"/></svg></div>
</section>

<main>
  <section class="abs panel learn">
    <h2>LEARN <b>About Pet Insurance</b></h2>
    <p>Lorem ipsum dolor sit amet, consectetuer adipiscing elit, sed diam nonummy nibh isaincidunt ut laoreet dolore magna aliquam erat volutpat. Ut wisi enim ad minim veniam, quisstruexerci tation ullamcorper suscipit lobortis nisl ut aliquip accumsan et iusto odio enim..</p>
    <div class="cols">
      <ul class="bul">
        <li>Vet Fees Cover Types</li>
        <li>What to Consider before Buying</li>
        <li>Ten Popular Pet Insurance Providers</li>
        <li>Confused by Pet Insurance:&nbsp; Start Here!</li>
        <li>Third Party Liability Insurance</li>
      </ul>
      <ul class="bul">
        <li>Six Vet Fees Pet Insurance Companies Won't Pay!</li>
        <li>Why Cheap Pet Insurance is Risky</li>
        <li>Why Your Pets Vet History is Important</li>
      </ul>
    </div>
    <span class="more" style="top:138px">Read More</span>
  </section>

  <section class="abs panel research">
    <h2 style="color:#1a2b40">Research <b>UK Pet Insurance Policies</b></h2>
    <p class="sub">Analysis, Customer Reviews and Full Details of All UK Policies</p>
    <div class="cols">
      <ul class="bul">
        <li>Critter Friends</li><li>Argent</li><li>Straight Path</li><li>E&amp;M</li><li>Hearty Pets</li><li>Helpshield</li><li>James Lowell</li><li>Lakeside Harbour</li>
      </ul>
      <ul class="bul">
        <li>Kennel Circle</li><li>P&amp;R</li><li>Beyond Pet Insurance</li><li>Petwise</li><li>Sandbury's Finance</li><li>Tesmark</li><li>Vantage Money</li><li>Other Providers</li>
      </ul>
    </div>
    <p class="cta">Search Our Database For Policies Matching Your Criteria<br>Compare Claims Experiences&nbsp; For Pet Insurance Providers</p>
    <span class="more" style="top:194px">Read More</span>
  </section>

  <section class="abs panel campaign">
    <h2>Campaign <b>For Fairer Pet Insurance</b></h2>
    <p style="margin-top:10px">Loremre ipsum dolor sit amet, consectetuer adipiscing elit, sed diam nonummy nibh rerunt ut laoreet dolore magna aliquam erat volutpat. Ut wisi enim ad minim veniam, quis loremis nostruexerci tation ullamcorper suscipit lobortis nisl.</p>
    <p>Loremre ipsum dolor sit amet, consectetuer adipiscing elit, sed diam nonummy nibh rerunt ut laoreet dolore magna aliquam erat volutpat.</p>
    <p>Loremre ipsum dolor sit amet, consectetuer adipiscing elit, sed diam nonummy nibh rerunt ut laoreet dolore magna aliquam erat volutpat. Ut wisi enim ad minim veniam, quis loremis nostruexerci tation ullamcorper suscipit.</p>
    <span class="more" style="top:131px">Read More</span>
  </section>

  <section class="abs popular">
    <h2>Popular <span>Resources</span></h2>
    <p>Loremre ipsum dolor sit amet, consectetuer adipiscing elit, sed diam nonummy nibh rerunt ut laoreet dolore magna aliquam erat volutpat.</p>
    <div class="row"><span>Lorem Ipsum</span><span>Lorem Ipsum</span></div>
    <span class="more dark" style="top:56px">Read More</span>
  </section>
</main>

<aside>
  <div class="abs ad" style="top:293px">
    <div class="brand">Pawsure</div>
    <div class="slogan">Everyday health cover for pets.</div>
    <div class="pup" role="img" aria-label="Puppy playing with a ball"></div>
    <ul>
      <li><svg width="10" height="8" viewBox="0 0 12 10"><path d="M1 5l3.5 3.5L11 1" stroke="#b3233b" stroke-width="2.2" fill="none"/></svg>Single Policy</li>
      <li><svg width="10" height="8" viewBox="0 0 12 10"><path d="M1 5l3.5 3.5L11 1" stroke="#b3233b" stroke-width="2.2" fill="none"/></svg>Most Bills Paid</li>
      <li><svg width="10" height="8" viewBox="0 0 12 10"><path d="M1 5l3.5 3.5L11 1" stroke="#b3233b" stroke-width="2.2" fill="none"/></svg>No Annual Cap</li>
    </ul>
    <div class="quote">GET A PRICE ▸</div>
    <div class="offer">Save $10 when you join</div>
    <div class="fine">Terms and conditions apply. Read policy wording.</div>
  </div>

  <div class="abs card bio">
    <h3>Biography</h3>
    <div class="portrait" role="img" aria-label="German shepherd puppy portrait"></div>
    <div class="who">Lorem Ispum<br>Autem</div>
    <div class="who2">Lorem Isum, Autem</div>
    <div class="txt">
      <p>Ut wisi enim ad minim veniam, quis nostrud exerc ree orper suscipit lobortis nisl ut aliquip ex ea commodor consequat. Duis autem vel eum. Lorem ipsum is ther dummpy text of the instury.</p>
      <p>Ut wisi enim ad minim veniam, quis nostrud exerc ullamcade orper suscipit lobortis.</p>
    </div>
    <span class="more dark" style="top:153px;font-family:'Open Sans',sans-serif">Read More</span>
  </div>

  <div class="abs card disc">
    <h3>Disclaimer</h3>
    <p>Please note that pet insurance terms often change. Whilst we will do our best to keep this website up to date you must check with the appropriate insurer before making any decisions. If you find any mistakes on this website please do let us know so we can correct it for the benefit of future visitors. Many thanks! -</p>
    <p class="see">See more at:</p>
    <p>www.pet-cover-polls.co.uk/pet-cover-companies/#sthash.opsYNKzp.dpuf</p>
  </div>

  <div class="abs ad small" style="top:814px">
    <div class="brand">Pawsure</div>
    <div class="slogan">Everyday health cover for pets.</div>
    <div class="pup" role="img" aria-label="Puppy playing with a ball"></div>
    <ul>
      <li><svg width="9" height="7" viewBox="0 0 12 10"><path d="M1 5l3.5 3.5L11 1" stroke="#b3233b" stroke-width="2.2" fill="none"/></svg>Single Policy</li>
      <li><svg width="9" height="7" viewBox="0 0 12 10"><path d="M1 5l3.5 3.5L11 1" stroke="#b3233b" stroke-width="2.2" fill="none"/></svg>Most Bills Paid</li>
      <li><svg width="9" height="7" viewBox="0 0 12 10"><path d="M1 5l3.5 3.5L11 1" stroke="#b3233b" stroke-width="2.2" fill="none"/></svg>No Annual Cap</li>
    </ul>
    <div class="quote">GET A PRICE ▸</div>
    <div class="offer">Save $10 when you join</div>
    <div class="fine">Terms and conditions apply. Read policy wording.</div>
  </div>
</aside>

<div class="abs pet-left" role="img" aria-label="German shepherd looking up"></div>
<div class="abs pet-right" role="img" aria-label="Burmese cat sitting"></div>

<footer>
  <div class="abs footer"></div>

  <div class="abs widget fb">
    <div class="head">Join us on Friendspace</div>
    <div class="page">
      <div class="avatar" role="img" aria-label="Page profile photo"></div>
      <div><div class="name">Pet Cover Polls UK</div><span class="likebtn">Like</span> <span style="font:6px Arimo,sans-serif">1,176</span></div>
    </div>
    <div class="post">
      <div class="meta"><div class="avatar" role="img" aria-label="Page profile photo"></div><div class="name">Pet Cover Polls<br>UK<small>January 18 at 11:43pm</small></div></div>
      <p>Pet Insurance Premium Increases</p>
      <p style="margin-top:3px">Interesting article from Consumer Watch suggesting that that pet insurance premiums can double as your pet ages...</p>
      <p style="margin-top:3px">Have to confess that this sounds on the low side to me! Would be really interested to hear how much yours</p>
    </div>
  </div>

  <div class="abs widget tw">
    <div class="head">Latest from Chirper</div>
    <div class="bar">Tweets <span>Follow</span></div>
    <div class="tweet" style="padding-top:2px"><div class="body">have already completed our survey:<br><a>polls.link/7kTq2Rm</a></div></div>
    <div class="tweet"><div class="avatar" role="img" aria-label="Account photo"></div><div class="body"><div class="top"><b>PetCover Polls</b><span class="dim">26 Sep</span></div><span class="dim">@PetCoverPolls</span><br>Know someone who has made a pet insurance claim in the last year? Please ask them to tell us about it. Please RT!<br><a>polls.link/R4nXe</a><br><span class="dim">Expand</span></div></div>
    <div class="tweet" style="border:0"><div class="avatar" role="img" aria-label="Account photo"></div><div class="body"><div class="top"><b>PetCover Polls</b><span class="dim">26 Sep</span></div><span class="dim">@PetCoverPolls</span></div></div>
    <div class="input">Tweet to @PetCoverPolls</div>
  </div>

  <div class="abs follow-title">Follow Us</div>
  <div class="abs sbtn" style="top:993px;width:153px"><i></i>Follow @PetCoverPolls</div>
  <div class="abs sbtn" style="top:1015px;width:46px"><i></i>Like</div>
  <div class="abs sbtn" style="top:1037px;width:74px"><i></i>Follow</div>

  <div class="abs foot-title">THE ANIMAL COVER<br>HANDBOOK 2015</div>

  <div class="abs copy">Copyright © 2015.&nbsp; TheAnimalCoverHandbook2015.&nbsp; All Rights Reserved.</div>
</footer>
</body>
</html>
```